Law Firm Business Card

This is a business card for a law firm that serves US military and veterans.

The card must have ONLY the following (we want an uncluttered look):

- Company logo (PNG, GIF, JPEG copies uploaded)
- A tagline reading: "a law firm for service members and veterans"
- My name and title: "Martin Okello" and "Attorney"
- My email: "martin.okello@harborlinecounsel.com"
- My number: "855-FILE-NOW (345-3669)"

We are looking for a clean, simple layout with only the above information, likely printed on a bright white cotton stock. The font of our logo is DIN 1451, and the font used on our website is Helvetica Neue. The color of our logo is #336699, and we probably want the tagline in that color also, and my contact information in a dark grey. Please review our website at www.harborlinecounsel.com to ensure your card design complements our website style.

Thanks and we look forward to seeing your submissions.

A few notes:

- Two-sided submissions are ok
- Please don't add graphics (scales of justice, judges hammer, etc)

```html
<!DOCTYPE html>
<html lang="en">
<head>
<meta charset="utf-8">
<title>Harborline Counsel – Business Card</title>
<link rel="stylesheet" href="https://fonts.googleapis.com/css2?family=Arimo:wght@400;700&display=swap">
<style>
  :root {
    --brand: #336699;
    --paper: #ffffff;
    --backdrop: #ececec;
    --band-text: #ffffff;
    --card-shadow: rgba(0, 0, 0, 0.18);
  }
  * { box-sizing: border-box; margin: 0; padding: 0; }
  html, body {
    width: 1200px;
    height: 1000px;
    overflow: hidden;
  }
  body {
    background: var(--backdrop);
    font-family: "Arimo", "Helvetica Neue", Helvetica, Arial, sans-serif;
    position: relative;
  }
  .card {
    position: absolute;
    left: 250px;
    width: 700px;
    height: 400px;
    background: var(--paper);
    box-shadow: 0 6px 18px var(--card-shadow);
    overflow: hidden;
  }
  .card--front { top: 70px; }
  .card--back  { top: 530px; }

  /* Company name (plain, one colour, one weight) */
  .company-name {
    color: var(--brand);
    font-weight: 700;
    white-space: nowrap;
  }

  /* Front */
  .card--front .company-name {
    position: absolute;
    left: 0;
    right: 0;
    top: 150px;
    text-align: center;
    font-size: 58px;
    line-height: 1;
  }
  .tagline {
    position: absolute;
    left: 0;
    right: 0;
    bottom: 62px;
    text-align: center;
    color: var(--brand);
    font-size: 25px;
    font-weight: 400;
  }

  /* Back */
  .card--back .company-name {
    position: absolute;
    top: 40px;
    right: 44px;
    font-size: 28px;
    line-height: 1;
  }
  .person {
    position: absolute;
    left: 0;
    right: 0;
    top: 128px;
    text-align: center;
    color: var(--brand);
  }
  .person__name {
    font-size: 32px;
    font-weight: 700;
  }
  .person__title {
    font-size: 24px;
    font-weight: 400;
    margin-top: 6px;
  }
  .contact-band {
    position: absolute;
    left: 0;
    right: 0;
    bottom: 38px;
    height: 130px;
    background: var(--brand);
    color: var(--band-text);
    display: flex;
    flex-direction: column;
    justify-content: center;
    align-items: center;
    font-size: 25px;
    line-height: 1.4;
  }
</style>
</head>
<body>

  <section class="card card--front" aria-label="Business card front">
    <p class="company-name">Harborline Counsel</p>
    <p class="tagline">a law firm for service members and veterans</p>
  </section>

  <section class="card card--back" aria-label="Business card back">
    <p class="company-name">Harborline Counsel</p>
    <div class="person">
      <p class="person__name">Martin Okello</p>
      <p class="person__title">Attorney</p>
    </div>
    <div class="contact-band">
      <p class="contact-band__email">e: martin.okello@harborlinecounsel.com</p>
      <p class="contact-band__phone">t: 855-FILE-NOW (345-3669)</p>
    </div>
  </section>

</body>
</html>
```